Golf Day Flyer - Hartwell School

Flyer for a golf day.
Parents and friends of a school are invited to play golf on Monday 22nd October.

Flyer from last year (2017) is attached. We would like to make the flyer more fun/humorous this year.

The golf day has two sessions: (1) Round of golf starting at 9AM and (2) Golf Clinic for beginner golfers.

So the flyer could have two sections - one showing experienced golfers, the other showing beginner golfers.

We have not finalised all the content for the flyer yet but need to look at some designs before we give all the content.

Target Market(s)

parents and friends of the school students - professionals (accountants, lawyers, doctors, etc)

Industry/Entity Type

Golf Course

Font styles to use
Serif

Colors

Designer to choose colors to be used in the design.

Requirements
Must have
• Refer to content attached document
Nice to have
• Funny golf pictures
Should not have
• N/A

```html
<!DOCTYPE html>
<html lang="en">
<head>
<meta charset="UTF-8">
<title>Hartwell Golf Day 2018</title>
<link rel="stylesheet" href="https://fonts.googleapis.com/css2?family=Audiowide&family=Open+Sans:ital,wght@0,400;0,700;1,400&display=swap">
<style>
  :root {
    --grass-light: #5fa83a;
    --grass-mid: #3f8a26;
    --grass-deep: #2a6418;
    --banner-top: #6ad61a;
    --banner-bottom: #3fa40c;
    --forest: #1f4a14;
    --panel: rgba(22, 30, 22, 0.9);
    --accent: #d2ee3c;
    --white: #ffffff;
    --footer: #0f3511;
    --ball: #e9ecec;
  }
  * { margin: 0; padding: 0; box-sizing: border-box; }
  html, body { width: 856px; height: 1200px; overflow: hidden; background: #ffffff; }
  .flyer {
    position: relative;
    width: 856px;
    height: 1200px;
    overflow: hidden;
    font-family: "Open Sans", Arial, sans-serif;
  }
  .fairway-photo {
    position: absolute; inset: 0;
    background:
      radial-gradient(ellipse 200px 70px at 430px 700px, #1c3a12 0%, rgba(28,58,18,0.6) 60%, rgba(28,58,18,0) 100%),
      linear-gradient(180deg, var(--grass-mid) 0%, #4b9a2c 45%, var(--grass-light) 75%, var(--grass-deep) 100%);
  }
  .sky { position: absolute; left: 0; top: 0; width: 856px; height: 340px; }
  .golfer-figure {
    position: absolute; left: 292px; top: 110px; width: 132px; height: 172px;
    background: var(--forest);
    border-radius: 40px 40px 6px 6px;
  }
  .title-banner {
    position: absolute; left: 300px; top: 210px; width: 538px; height: 107px;
    border-radius: 24px;
    background: linear-gradient(180deg, var(--banner-top), var(--banner-bottom));
    color: var(--white);
  }
  .title-banner .school {
    position: absolute; left: 80px; top: 33px;
    font-family: "Audiowide", sans-serif; font-size: 42px; letter-spacing: -1px; line-height: 1;
    white-space: nowrap;
  }
  .title-banner .event {
    position: absolute; top: 28px; height: 54px;
    font-family: "Open Sans", sans-serif; font-weight: 700; font-size: 12px; line-height: 1;
    writing-mode: vertical-rl; transform: rotate(180deg);
    letter-spacing: 1px; text-align: left;
  }
  .title-banner .event--golf { left: 366px; }
  .title-banner .event--day { left: 381px; }
  .title-banner .year {
    position: absolute; right: 12px; top: 33px;
    font-family: "Audiowide", sans-serif; font-size: 42px; line-height: 1; letter-spacing: -1px;
    white-space: nowrap;
  }
  .session {
    position: absolute; top: 560px; width: 246px; height: 246px;
    background: var(--panel); border-radius: 20px;
    text-align: center;
  }
  .session--round { left: 12px; }
  .session--clinic { left: 586px; }
  .session-photo {
    position: absolute; width: 192px; height: 192px; border-radius: 50%;
    border: 5px solid var(--forest);
  }
  .session-photo--round {
    left: 38px; top: 450px;
    background: linear-gradient(160deg, #9fd35a 0%, #5f9e2e 55%, #2f3a4a 100%);
  }
  .session-photo--clinic {
    left: 612px; top: 450px;
    background: linear-gradient(180deg, #8fb8e0 0%, #2f5a2a 35%, #58a034 60%, #3f8a26 100%);
  }
  .session .time {
    position: absolute; left: 0; right: 0; top: 100px;
    font-family: "Audiowide", sans-serif; font-size: 13px; color: var(--white); letter-spacing: 1px;
  }
  .session .detail {
    position: absolute; left: 0; right: 0; top: 136px;
    font-size: 16px; line-height: 20px; color: var(--accent); letter-spacing: 1px;
  }
  .date-ball {
    position: absolute; left: 322px; top: 664px; width: 224px; height: 224px; border-radius: 50%;
    background: radial-gradient(circle at 40% 35%, #ffffff 0%, var(--ball) 55%, #b9c0c0 100%);
    text-align: center;
    box-shadow: 0 6px 20px rgba(0,0,0,0.35);
  }
  .date-ball .day {
    display: block; margin-top: 36px;
    font-family: "Audiowide", sans-serif; font-size: 108px; line-height: 108px; color: var(--forest);
  }
  .date-ball .month {
    display: block; margin-top: 8px;
    font-weight: 700; font-size: 18px; letter-spacing: 1px; color: #2d3d2a;
  }
  .lunch {
    position: absolute; left: 185px; top: 910px; width: 495px; height: 186px;
    background: var(--panel); border-radius: 20px;
    text-align: center; color: var(--white);
    font-size: 16px; letter-spacing: 1px; line-height: 22px;
  }
  .lunch h2 {
    font-family: "Audiowide", sans-serif; font-weight: 400; font-size: 22px; letter-spacing: 1px;
    margin-top: 14px; margin-bottom: 12px;
  }
  .lunch .label { color: var(--accent); }
  .lunch .payment { margin-top: 28px; text-align: left; padding-left: 56px; }
  .lunch .payment p + p { margin-top: 5px; padding-left: 18px; }
  .footer {
    position: absolute; left: 0; top: 1124px; width: 856px; height: 76px;
    background: var(--footer);
    display: flex; align-items: center; justify-content: center;
    font-style: italic; font-size: 21px; color: var(--accent); letter-spacing: 1px;
  }
</style>
</head>
<body>
<main class="flyer">
  <div class="fairway-photo" role="img" aria-label="Close-up photo of a putting green with the golf hole"></div>

  <svg class="sky" viewBox="0 0 856 340" role="img" aria-label="Illustrated sunny sky with clouds above the sea">
    <defs>
      <linearGradient id="skyFill" x1="0" y1="0" x2="0" y2="1">
        <stop offset="0" stop-color="#52e0dc"/>
        <stop offset="0.6" stop-color="#e6fbfa"/>
        <stop offset="1" stop-color="#7fd8e0"/>
      </linearGradient>
    </defs>
    <path d="M0 0 H856 V190 Q430 350 0 302 Z" fill="url(#skyFill)"/>
    <path d="M0 302 Q430 350 856 190 L856 196 Q430 356 0 308 Z" fill="#ffffff"/>
  </svg>

  <div class="golfer-figure" role="img" aria-label="Silhouette of a golfer finishing a swing"></div>

  <header class="title-banner">
    <span class="school">HARTWELL</span>
    <span class="event event--golf">GOLF</span>
    <span class="event event--day">DAY</span>
    <span class="year">2018</span>
  </header>

  <section class="session session--round">
    <p class="time">9:00 A.M- 11:00 A.M</p>
    <p class="detail">Shot gun Start for 18<br>hole players</p>
  </section>
  <div class="session-photo session-photo--round" role="img" aria-label="Photo of golfers lining up a shot on the course"></div>

  <section class="session session--clinic">
    <p class="time">11.30AM - 12:00P.M</p>
    <p class="detail">Clinic with a Golf<br>Pro for non-Golfers</p>
  </section>
  <div class="session-photo session-photo--clinic" role="img" aria-label="Photo of a golfer teeing off on a fairway"></div>

  <div class="date-ball">
    <span class="day">22</span>
    <span class="month">OCTOBER 2018</span>
  </div>

  <section class="lunch">
    <h2>POST GOLF LUNCH</h2>
    <p><span class="label">From 1pm in the Dining Room</span></p>
    <p><span class="label">Guest Speaker:</span> Daniel Mercer</p>
    <div class="payment">
      <p><span class="label">Payment:</span> www.example.com/payments</p>
      <p><span class="label">Pricing:</span> 30$</p>
    </div>
  </section>

  <footer class="footer">A combined Hartwell Old Scholars and Parents &amp; Friends Function.</footer>
</main>
</body>
</html>
```